Vitara Care needs new labels for a new line of natural vitamins and supplements

We are a dutch based Vitara Care. We need labels for a new line of healthy, all natural, vitamins and supplements line.
We came across this brand: http://www.velmora.eu , we like that style so you can use this as inspiration.
Key words : Natural , Organic logo's , clear , earthy colors , open , trustworthy , healthy
The product should be leading, the logo/brandname can be small, even only mentioned on the rear label.

Target Market(s)

Health conscious people

Industry/Entity Type

Health And Wellness

Requirements
Must have
• A clear , simple, trustworthy , organic style

```html
<!DOCTYPE html>
<html lang="en">
<head>
<meta charset="utf-8">
<title>Vitamin Support Labels</title>
<link rel="stylesheet" href="https://fonts.googleapis.com/css2?family=Open+Sans:wght@400;600;700&display=swap">
<style>
  :root {
    --bg: #c69c72;
    --paper: #ffffff;
    --ink: #2a2a2a;
    --brown: #a2461c;
    --brown-soft: #e8bfa3;
    --brown-band: #d9a886;
    --green: #4aa63a;
    --green-soft: #cfe5b4;
    --green-band: #a9d07c;
    --teal: #137b7a;
    --teal-soft: #bfe0e3;
    --teal-band: #a4cfc9;
    --blue: #1f6db5;
    --brand: #1c8a3c;
    --stamp: #b6d39c;
  }
  * { box-sizing: border-box; margin: 0; padding: 0; }
  html, body { width: 1200px; height: 1050px; overflow: hidden; }
  body {
    background: radial-gradient(ellipse at 50% 40%, #dcb48a 0%, var(--bg) 70%);
    font-family: "Open Sans", sans-serif;
    color: var(--ink);
    position: relative;
  }
  .label {
    position: absolute;
    width: 420px;
    height: 460px;
    background: var(--paper);
    box-shadow: 0 10px 30px rgba(80, 50, 20, .25);
    overflow: hidden;
    transform-origin: top left;
    --accent: var(--green);
    --soft: var(--green-soft);
    --band: var(--green-band);
  }
  .label--center { left: 390px; top: 295px; }
  .label--left { left: 25px; top: 345px; transform: scale(.8); --accent: var(--brown); --soft: var(--brown-soft); --band: var(--brown-band); }
  .label--right { left: 839px; top: 345px; transform: scale(.8); --accent: var(--teal); --soft: var(--teal-soft); --band: var(--teal-band); }

  .ribbon {
    position: absolute; left: 145px; top: 0; width: 130px; height: 30px;
    background: var(--green); color: #fff; font-size: 13px;
    display: flex; align-items: center; justify-content: center;
  }
  .label--center .ribbon { background: var(--blue); }
  .stamp { position: absolute; left: 14px; top: 36px; }
  .product-icon {
    position: absolute; left: 155px; top: 45px; width: 110px; height: 110px;
    border-radius: 50%; background: var(--soft);
  }
  .rule { position: absolute; left: 75px; width: 270px; height: 1px; background: var(--accent); }
  .rule--top { top: 183px; }
  .rule--bottom { top: 326px; }
  .line {
    position: absolute; left: 0; width: 100%; display: flex; justify-content: center;
    align-items: center; gap: 36px; font-size: 16px;
  }
  .line::before, .line::after { content: ""; width: 4px; height: 4px; border-radius: 50%; background: var(--accent); }
  .tagline { top: 190px; }
  .form { top: 290px; font-size: 17px; font-weight: 600; }
  .product-name {
    position: absolute; left: 50px; top: 222px; width: 320px; height: 56px;
    border-radius: 10px; background: var(--accent); color: #fff;
    display: flex; align-items: center; justify-content: center;
    font-size: 27px; font-weight: 600; letter-spacing: .5px;
  }
  .count { position: absolute; top: 333px; width: 100%; text-align: center; font-size: 10px; }
  .band { position: absolute; left: 0; bottom: 0; width: 100%; height: 60px; background: var(--band); }
  .brand-box {
    position: absolute; left: 130px; bottom: 10px; width: 160px; height: 72px;
    background: var(--paper); border: 2px solid var(--accent); border-bottom: 0;
    display: flex; align-items: center; justify-content: center; gap: 6px;
  }
  .brand-box::before { content: ""; width: 10px; height: 10px; background: var(--brand); }
  .brand-name { font-size: 17px; font-weight: 700; color: var(--brand); }
</style>
</head>
<body>

<section class="label label--left">
  <div class="ribbon">100% NATURAL</div>
  <svg class="stamp" width="90" height="70" aria-hidden="true"><ellipse cx="45" cy="35" rx="40" ry="28" fill="none" stroke="var(--stamp)" stroke-width="4" transform="rotate(-12 45 35)"/></svg>
  <div class="product-icon" role="img" aria-label="Leaves and capsule illustration"></div>
  <div class="rule rule--top"></div>
  <p class="line tagline">Heart and Skin Health</p>
  <h2 class="product-name">VITAMIN SUPPORT</h2>
  <p class="line form">IN CAPSULES</p>
  <div class="rule rule--bottom"></div>
  <p class="count">60 Coated Capsules</p>
  <div class="band"></div>
  <div class="brand-box"><span class="brand-name">Vitara Care</span></div>
</section>

<section class="label label--center">
  <div class="ribbon">100% NATURAL</div>
  <svg class="stamp" width="90" height="70" aria-hidden="true"><ellipse cx="45" cy="35" rx="40" ry="28" fill="none" stroke="var(--stamp)" stroke-width="4" transform="rotate(-12 45 35)"/></svg>
  <div class="product-icon" role="img" aria-label="Apple outline with capsules illustration"></div>
  <div class="rule rule--top"></div>
  <p class="line tagline">Brain, and Joint Health</p>
  <h1 class="product-name">VITAMIN SUPPORT</h1>
  <p class="line form">IN CAPSULES</p>
  <div class="rule rule--bottom"></div>
  <p class="count">60 Coated Capsules</p>
  <div class="band"></div>
  <div class="brand-box"><span class="brand-name">Vitara Care</span></div>
</section>

<section class="label label--right">
  <div class="ribbon">100% NATURAL</div>
  <svg class="stamp" width="90" height="70" aria-hidden="true"><ellipse cx="45" cy="35" rx="40" ry="28" fill="none" stroke="var(--stamp)" stroke-width="4" transform="rotate(-12 45 35)"/></svg>
  <div class="product-icon" role="img" aria-label="Leaves and capsule illustration"></div>
  <div class="rule rule--top"></div>
  <p class="line tagline">Heart and Skin Health</p>
  <h2 class="product-name">VITAMIN SUPPORT</h2>
  <p class="line form">IN CAPSULES</p>
  <div class="rule rule--bottom"></div>
  <p class="count">60 Coated Capsules</p>
  <div class="band"></div>
  <div class="brand-box"><span class="brand-name">Vitara Care</span></div>
</section>

</body>
</html>
```